Business Card cabinets and cabinets components making company.

the card should be formal and interesting at the same time. The main colors will be black and white.

Font styles to use
Sans Serif

Colors

Designer to choose only greyscale colors for use in the design.

Requirements
Must have
• At least must have the followings:
office phone
cell phone
address
position
name
email
web

```html
<!DOCTYPE html>
<html lang="en">
<head>
<meta charset="utf-8">
<title>Trimfold — Business Card</title>
<link href="https://fonts.googleapis.com/css2?family=Open+Sans:wght@400;700&display=swap" rel="stylesheet">
<style>
  :root {
    --backdrop: #3a3633;
    --card-face: #2e2e2e;
    --card-back: #232323;
    --pattern-tone: #2c2c2c;
    --ink: #ffffff;
    --ink-soft: #e6e6e6;
  }
  * { box-sizing: border-box; margin: 0; padding: 0; }
  html, body { width: 1200px; height: 795px; overflow: hidden; }
  body {
    background: var(--backdrop);
    font-family: "Open Sans", Arial, sans-serif;
    color: var(--ink);
    position: relative;
  }
  .card {
    position: absolute;
    top: 243px;
    width: 540px;
    height: 309px;
    border-radius: 3px;
    overflow: hidden;
  }
  .card--back { left: 40px; background: var(--card-back); }
  .card--front { left: 620px; background: var(--card-face); }

  .pattern-field {
    position: absolute;
    inset: 0;
    background: linear-gradient(135deg, #262626, var(--pattern-tone) 50%, #202020);
  }
  .brand {
    display: flex;
    align-items: center;
    gap: 8px;
    font-weight: 700;
    color: var(--ink);
    white-space: nowrap;
  }
  .brand__mark { background: var(--ink); flex: none; }
  .card--back .brand {
    position: absolute;
    left: 205px;
    top: 205px;
    font-size: 30px;
  }
  .card--back .brand__mark { width: 14px; height: 14px; }

  .card--front .brand {
    position: absolute;
    left: 36px;
    top: 128px;
    font-size: 40px;
  }
  .card--front .brand__mark { width: 18px; height: 18px; }
  .brand-rule {
    position: absolute;
    left: 36px;
    top: 186px;
    width: 220px;
    height: 2px;
    background: var(--ink);
  }
  .divider {
    position: absolute;
    left: 290px;
    top: 60px;
    width: 1.5px;
    height: 190px;
    background: var(--ink);
  }
  .contact {
    position: absolute;
    left: 306px;
    top: 64px;
    font-size: 13.5px;
    line-height: 1.38;
    color: var(--ink-soft);
  }
  .contact__name { font-weight: 700; font-size: 16px; color: var(--ink); letter-spacing: .3px; }
  .contact__role { margin-bottom: 8px; }
  .contact__address { margin-bottom: 4px; }
  .contact__row { display: flex; align-items: center; gap: 6px; }
  .contact__row svg { width: 11px; height: 11px; flex: none; }
</style>
</head>
<body>
  <section class="card card--back">
    <div class="pattern-field" role="img" aria-label="Embossed repeating geometric brand pattern in dark grey"></div>
    <div class="brand"><span class="brand__mark"></span>Trimfold</div>
  </section>

  <section class="card card--front">
    <div class="brand"><span class="brand__mark"></span>Trimfold</div>
    <div class="brand-rule"></div>
    <div class="divider"></div>
    <div class="contact">
      <p class="contact__name">DORIAN VALE</p>
      <p class="contact__role">Founder &amp; CEO</p>
      <p class="contact__address">Address line, Suite code<br>State, 3573, Country</p>
      <p class="contact__row">
        <svg viewBox="0 0 12 12" aria-hidden="true"><path d="M2.5 1h2l1 3-1.5 1a6 6 0 0 0 3 3l1-1.5 3 1v2A1.5 1.5 0 0 1 9.5 11 8.5 8.5 0 0 1 1 2.5 1.5 1.5 0 0 1 2.5 1z" fill="#fff"/></svg>
        (555) 014-2290
      </p>
      <p class="contact__row">
        <svg viewBox="0 0 12 12" aria-hidden="true"><rect x="3" y="0.8" width="6" height="10.4" rx="1" fill="none" stroke="#fff" stroke-width="1.2"/><circle cx="6" cy="9.4" r=".7" fill="#fff"/></svg>
        (555) 014-2291
      </p>
      <p class="contact__row">
        <svg viewBox="0 0 12 12" aria-hidden="true"><rect x="0.5" y="2.5" width="11" height="7" fill="#fff"/><path d="M0.5 2.5 6 6.6 11.5 2.5" fill="none" stroke="#2e2e2e" stroke-width="1"/></svg>
        hello@trimfold.example
      </p>
      <p class="contact__row">
        <svg viewBox="0 0 12 12" aria-hidden="true"><circle cx="6" cy="6" r="5" fill="none" stroke="#fff" stroke-width="1.1"/><ellipse cx="6" cy="6" rx="2.2" ry="5" fill="none" stroke="#fff" stroke-width="1"/><path d="M1 6h10" stroke="#fff" stroke-width="1"/></svg>
        www.trimfold.example
      </p>
    </div>
  </section>
</body>
</html>
```